Mental Health care Company in Washington DC

We are a new mental health care services provider in Washington DC. Please look at these sites.
https://quarrystonewellbeingpartners.com
https://www.quietharborllc.com
https://fernvale-nb.org/
https://www.truepathnb.com
https://www.willowmeadnb.com

```html
<!DOCTYPE html>
<html lang="en">
<head>
<meta charset="utf-8">
<title>Lumen Mind Services — Mental Health Care in Washington DC</title>
<link href="https://fonts.googleapis.com/css2?family=Poppins:wght@300;400;500;600;700&family=Kaushan+Script&display=swap" rel="stylesheet">
<style>
:root{
  --navy:#0f2346;
  --ink:#1b2b45;
  --text:#3f4654;
  --muted:#6b7280;
  --teal:#5fc0c7;
  --teal-soft:#a9dde0;
  --teal-pale:#e9f5f5;
  --orange:#f28024;
  --white:#ffffff;
}
*{box-sizing:border-box;margin:0;padding:0}
html,body{width:1200px;height:4175px;overflow:hidden}
body{font-family:"Poppins",sans-serif;color:var(--text);background:var(--white);position:relative}
section,header,footer{position:absolute;left:0;width:1200px}
.abs{position:absolute}
.photo{position:absolute}

/* header */
.site-header{top:0;height:94px;background:var(--white);z-index:3}
.brand{position:absolute;left:141px;top:24px;display:flex;align-items:center;gap:10px}
.brand-dot{width:12px;height:12px;border-radius:50%;background:var(--orange)}
.brand-name{font-weight:500;font-size:30px;color:var(--navy);letter-spacing:-0.5px;line-height:1}
.brand-sub{position:absolute;left:164px;top:60px;font-size:10px;letter-spacing:6px;color:var(--muted)}
.main-nav{position:absolute;left:527px;top:38px;display:flex;gap:45px;font-size:12px;font-weight:500;color:var(--ink)}
.nav-cta{position:absolute;left:932px;top:26px;width:128px;height:42px;background:var(--teal-soft);color:var(--ink);font-size:12px;font-weight:500;display:flex;align-items:center;justify-content:center;border-radius:2px}

/* hero */
.hero{top:94px;height:668px;overflow:hidden;background:linear-gradient(90deg,#e9eef3 0%,#eef2f6 45%,#dfe6ec 100%)}
.hero .photo{left:535px;top:0;width:665px;height:620px;background:linear-gradient(120deg,#cfd9e2 0%,#b9c6d2 40%,#e6e1dc 70%,#9aa7b2 100%)}
.hero-copy{position:absolute;left:143px;top:126px}
.hero-kicker{font-size:33px;color:var(--ink);font-weight:400;line-height:46px}
.hero-title{font-size:42px;font-weight:700;color:var(--ink);line-height:52px}
.hero-loc{font-size:33px;color:var(--ink);line-height:46px}
.hero-lead{font-size:17px;color:var(--ink);line-height:25px;margin-top:14px}
.btn-teal{margin-top:30px;width:202px;height:40px;background:var(--teal-soft);color:var(--ink);font-size:12px;font-weight:500;display:flex;align-items:center;justify-content:center;border-radius:2px}
.hero-wave{position:absolute;left:0;bottom:0}

/* features */
.features{top:820px;height:130px}
.feature{position:absolute;top:22px;width:300px}
.feature-icon{position:absolute;left:0;top:0;width:62px;height:62px;border-radius:50%;border:1px solid #e6e6e6;display:flex;align-items:center;justify-content:center}
.feature h3{position:absolute;left:83px;top:0;font-size:15px;font-weight:500;color:var(--ink);white-space:nowrap}
.feature p{position:absolute;left:83px;top:30px;font-size:11px;line-height:18px;color:var(--muted);width:210px}
.rule{position:absolute;left:102px;top:992px;width:994px;height:1px;background:#cfcfcf}

/* question band */
.ask{top:1066px;left:141px;width:918px;height:207px;border-radius:26px;overflow:hidden;background:linear-gradient(90deg,var(--orange) 0%,#f5924a 45%,#f7b27a 65%,#eee9e5 80%)}
.ask .photo{right:0;top:0;width:290px;height:207px;background:linear-gradient(90deg,rgba(240,236,232,0) 0%,#e7e3df 30%,#d9dde2 70%,#c9d3dc 100%)}
.ask-script{position:absolute;left:68px;top:40px;font-family:"Kaushan Script",cursive;font-size:21px;color:#ffe2a8}
.ask-title{position:absolute;left:68px;top:68px;font-size:23px;font-weight:500;line-height:34px;color:var(--white)}
.ask-link{position:absolute;left:68px;top:144px;font-size:14px;font-weight:500;color:var(--white);text-decoration:underline}
.pills{top:1170px;left:1105px;width:95px;height:110px;background:radial-gradient(circle at 40% 50%,#c9dde6 0%,rgba(255,255,255,0) 70%)}

/* marquee */
.marquee{top:1358px;height:50px;background:var(--teal);display:flex;align-items:center;gap:20px;white-space:nowrap;color:var(--white);font-size:15px}
.marquee span{display:flex;align-items:center;gap:18px}
.marquee svg{flex:none}

/* about */
.about{top:1408px;height:568px}
.about-bg{position:absolute;left:0;top:0;width:605px;height:568px;background:var(--teal-pale)}
.about-divider{position:absolute;left:605px;top:0;width:1px;height:568px;background:#d7e3e4}
.about .photo{left:0;top:86px;width:519px;height:396px;border-radius:0 16px 16px 0;background:linear-gradient(135deg,#4f8fb8 0%,#7fb4d4 45%,#e6ebef 75%,#c8d3dc 100%)}
.eyebrow{font-size:14px;font-weight:500;color:var(--teal);letter-spacing:0.3px;display:flex;align-items:center;gap:10px}
.about-copy{position:absolute;left:673px;top:92px;width:440px}
.about-copy h2{font-size:32px;font-weight:600;color:var(--ink);line-height:38px;margin-top:18px}
.about-copy p{font-size:12.5px;line-height:22.7px;color:var(--text);margin-top:16px}
.btn-orange{margin-top:22px;width:195px;height:36px;border-radius:18px;background:var(--orange);color:var(--white);font-size:12px;font-weight:500;display:flex;align-items:center;justify-content:center}

/* services */
.services{top:2050px;height:480px}
.section-head{position:absolute;left:0;width:1200px;text-align:center}
.services .label{top:12px;font-size:14px;color:var(--teal);font-weight:500}
.head-rule{position:absolute;left:560px;top:46px;width:80px;height:1px;background:var(--teal)}
.services h2{top:60px;font-size:30px;font-weight:500;color:var(--ink)}
.card{position:absolute;top:133px;width:282px;height:318px;border:1.5px solid #8d8d8d;border-bottom:none;background:var(--white)}
.card-bottom{position:absolute;bottom:0;height:1.5px;background:#8d8d8d;width:110px}
.card .photo{left:14px;top:16px;width:252px;height:140px}
.card h3{position:absolute;left:0;top:180px;width:100%;text-align:center;font-size:17px;font-weight:500;color:var(--ink)}
.card p{position:absolute;left:18px;top:214px;width:244px;text-align:center;font-size:12.5px;line-height:22.5px;color:var(--text)}
.card-icon{position:absolute;left:116px;top:294px;width:50px;height:50px;border-radius:50%;background:var(--teal);display:flex;align-items:center;justify-content:center;box-shadow:0 0 0 5px #d9f0f1}

/* journey */
.journey{top:2621px;height:402px;background:linear-gradient(90deg,#dfe3e6 0%,#eee5d9 35%,#f4c193 55%,#f28b35 75%,var(--orange) 100%)}
.journey .photo{left:0;top:0;width:640px;height:402px;background:linear-gradient(90deg,#c7ccd1 0%,#e9ddcd 40%,#f3d3b2 75%,rgba(244,176,118,0) 100%)}
.journey-copy{position:absolute;left:629px;top:90px;width:520px;color:var(--white)}
.journey-copy h2{font-size:32px;font-weight:500;line-height:47px;color:#fff6ec}
.journey-copy p{font-size:14px;line-height:26px;margin-top:22px;color:#fff2e4}
.btn-ghost{position:absolute;left:0;top:184px;width:247px;height:38px;border:1px solid var(--white);border-radius:19px;font-size:13px;font-weight:500;display:flex;align-items:center;justify-content:center;color:var(--white)}

/* values strip */
.values{top:3060px;height:120px;overflow:hidden}
.values-text{position:absolute;left:-141px;top:0;white-space:nowrap;font-size:72px;font-weight:600;letter-spacing:1px;line-height:120px}
.outline{color:transparent;-webkit-text-stroke:1.3px #8f8f8f}
.solid{color:var(--ink)}

/* testimonials */
.reviews{top:3215px;height:440px;overflow:hidden}
.reviews h2{top:8px;font-size:31px;font-weight:500;color:var(--ink);line-height:41px}
.review{position:absolute;top:142px;width:286px;height:244px;background:var(--white);box-shadow:0 4px 24px rgba(0,0,0,0.07)}
.quote{position:absolute;top:-22px;width:40px;height:40px;border-radius:50%;border:2px solid var(--teal);background:var(--white);display:flex;align-items:center;justify-content:center;font-size:26px;font-weight:700;color:var(--teal);line-height:1}
.quote.orange{border-color:var(--orange);color:var(--orange)}
.avatar{position:absolute;left:23px;top:22px;width:60px;height:60px;border-radius:50%;background:linear-gradient(160deg,#d9c9bb,#7c6e66)}
.stars{position:absolute;left:103px;top:40px;font-size:17px;letter-spacing:2px;color:#f5a623}
.stars .off{color:transparent;-webkit-text-stroke:1px #f5a623}
.review h4{position:absolute;left:23px;top:102px;font-size:13px;font-weight:500;color:var(--ink)}
.review p{position:absolute;left:23px;top:126px;width:240px;font-size:11px;line-height:20.5px;color:var(--text)}
.dots{position:absolute;left:557px;top:403px;display:flex;gap:8px}
.dots i{width:11px;height:11px;border-radius:50%;background:#d4d4d4}
.dots i.on{background:var(--orange)}

/* footer */
.site-footer{top:3711px;height:464px;background:var(--navy);color:#e7ebf2}
.foot-brand{position:absolute;left:141px;top:116px;display:flex;align-items:center;gap:10px}
.foot-brand .brand-name{color:var(--white)}
.foot-brand-sub{position:absolute;left:164px;top:150px;font-size:10px;letter-spacing:6px;color:#cfd6e2}
.foot-about{position:absolute;left:138px;top:188px;width:190px;font-size:12px;line-height:21px}
.foot-col{position:absolute;top:116px}
.foot-col h4{font-size:17px;font-weight:500;color:var(--orange);margin-bottom:16px}
.foot-col ul{list-style:none;font-size:12px;line-height:32px}
.foot-col ul li::before{content:"•";margin-right:8px}
.foot-col p{font-size:12px;line-height:21px}
.foot-col .k{color:var(--orange);margin-top:12px}
.stay{position:absolute;left:782px;top:86px;width:290px;height:253px;background:#1d3358;border-radius:10px;padding:26px 37px}
.stay h4{font-size:17px;font-weight:500;color:var(--orange)}
.stay p{font-size:12px;line-height:21px;margin-top:12px}
.email{position:absolute;left:37px;top:124px;width:216px;height:36px;background:var(--white);border-radius:18px;font-size:11px;color:#888;padding:0 20px;display:flex;align-items:center;justify-content:space-between}
.subscribe{position:absolute;left:37px;top:182px;width:150px;height:36px;background:var(--orange);border-radius:18px;font-size:12px;color:var(--white);display:flex;align-items:center;justify-content:space-around}
.foot-rule{position:absolute;left:0;top:408px;width:1200px;height:1px;background:#2b4066}
.foot-bottom{position:absolute;left:141px;top:430px;width:918px;display:flex;justify-content:space-between;font-size:12px}
</style>
</head>
<body>

<header class="site-header">
  <div class="brand"><span class="brand-dot"></span><span class="brand-name">Lumen Mind</span></div>
  <div class="brand-sub">SERVICES</div>
  <nav class="main-nav"><span>HOME</span><span>ABOUT US</span><span>SERVICES</span><span>OUR TEAM</span></nav>
  <div class="nav-cta">CONTACT US</div>
</header>

<section class="hero">
  <div class="photo" role="img" aria-label="Smiling young woman in a bright clinic talking with a counselor across a table"></div>
  <div class="hero-copy">
    <div class="hero-kicker">Compassionate</div>
    <div class="hero-title">Mental Health Care</div>
    <div class="hero-loc">in Washington DC</div>
    <p class="hero-lead">Your journey to wellness begins with understanding.<br>We're here to guide you every step of the way.</p>
    <div class="btn-teal">SCHEDULE CONSULTATION</div>
  </div>
  <svg class="hero-wave" width="1200" height="668" viewBox="0 0 1200 668">
    <path d="M0 530 C200 640 420 640 640 590 C840 545 1020 545 1200 560 L1200 668 L0 668 Z" fill="#ffffff"/>
  </svg>
</section>

<section class="features">
  <div class="feature" style="left:141px">
    <div class="feature-icon"><svg width="30" height="30" viewBox="0 0 30 30" fill="none" stroke="#f28024" stroke-width="1.6"><path d="M15 13c-2-4-8-2-6 2l6 5 6-5c2-4-4-6-6-2z"/><path d="M3 22c4-2 7-1 10 1h8"/></svg></div>
    <h3>Personalized Family Care</h3>
    <p>We treat you like family, building lasting relationships based on trust and compassion</p>
  </div>
  <div class="feature" style="left:451px">
    <div class="feature-icon"><svg width="30" height="30" viewBox="0 0 30 30" fill="none" stroke="#5fc0c7" stroke-width="1.6"><path d="M15 25C5 18 4 12 8 8s7 0 7 2c0-2 3-6 7-2s3 10-7 17z"/><path d="M15 12v6M12 15h6"/></svg></div>
    <h3>Comprehensive Services</h3>
    <p>From routine checkups to specialized testing, we offer a wide range of services to meet your needs</p>
  </div>
  <div class="feature" style="left:767px">
    <div class="feature-icon"><svg width="30" height="30" viewBox="0 0 30 30" fill="none" stroke="#f28024" stroke-width="1.6"><circle cx="15" cy="15" r="10"/><circle cx="15" cy="13" r="3"/><path d="M9 22c2-4 10-4 12 0"/></svg></div>
    <h3>Experienced &amp; Caring Staff</h3>
    <p>Our team of dedicated professionals is committed to providing the highest quality care</p>
  </div>
</section>
<div class="rule"></div>

<section class="ask">
  <div class="photo" role="img" aria-label="Doctor in a white coat holding a stethoscope"></div>
  <div class="ask-script">Have A Question?</div>
  <div class="ask-title">Reach out to schedule your appointment or<br>get answers to your questions</div>
  <div class="ask-link">Schedule an Appointment Today!</div>
</section>
<div class="abs pills" role="img" aria-label="Scattered capsules and a syringe"></div>

<section class="marquee">
  <span style="margin-left:-8px">te Care</span>
  <span><svg width="20" height="18" viewBox="0 0 20 18" fill="none" stroke="#fff" stroke-width="1.6"><path d="M10 16C2 10 1 6 4 3s6 0 6 2c0-2 3-5 6-2s2 7-6 13z"/></svg>Family-Focused</span>
  <span><svg width="20" height="18" viewBox="0 0 20 18" fill="none" stroke="#fff" stroke-width="1.6"><path d="M10 16C2 10 1 6 4 3s6 0 6 2c0-2 3-5 6-2s2 7-6 13z"/></svg>Comprehensive Services</span>
  <span><svg width="20" height="18" viewBox="0 0 20 18" fill="none" stroke="#fff" stroke-width="1.6"><path d="M10 16C2 10 1 6 4 3s6 0 6 2c0-2 3-5 6-2s2 7-6 13z"/></svg>Advanced Testing</span>
  <span><svg width="20" height="18" viewBox="0 0 20 18" fill="none" stroke="#fff" stroke-width="1.6"><path d="M10 16C2 10 1 6 4 3s6 0 6 2c0-2 3-5 6-2s2 7-6 13z"/></svg>Community Health</span>
  <span><svg width="20" height="18" viewBox="0 0 20 18" fill="none" stroke="#fff" stroke-width="1.6"><path d="M10 16C2 10 1 6 4 3s6 0 6 2c0-2 3-5 6-2s2 7-6 13z"/></svg>Personalized Healthcare</span>
  <span><svg width="20" height="18" viewBox="0 0 20 18" fill="none" stroke="#fff" stroke-width="1.6"><path d="M10 16C2 10 1 6 4 3s6 0 6 2c0-2 3-5 6-2s2 7-6 13z"/></svg>Comp</span>
</section>

<section class="about">
  <div class="about-bg"></div>
  <div class="about-divider"></div>
  <div class="photo" role="img" aria-label="Father holding his young son giving a high five to a smiling doctor"></div>
  <div class="about-copy">
    <div class="eyebrow">WHO WE ARE <svg width="56" height="2" viewBox="0 0 56 2"><line x1="0" y1="1" x2="56" y2="1" stroke="#5fc0c7" stroke-width="1"/></svg></div>
    <h2>A Trusted Mental Health<br>Partner In DC</h2>
    <p>Lorem Ipsum is simply dummy text of the printing and typesetting industry. Lorem Ipsum has been the industry's standard dummy text ever since the 1500s, when an unknown printer took a galley of type and scrambled it to make a type specimen book. It has survived not only five centuries, but also the leap into electronic typesetting, remaining essentially unchanged. It was popularised in the 1960s with the release of printed sample sheets containing Lorem Ipsum passages, and more recently with desktop layout software including many versions of Lorem Ipsum</p>
    <div class="btn-orange">Learn More About Us</div>
  </div>
</section>

<section class="services">
  <div class="section-head label">OUR CORE SERVICES</div>
  <div class="head-rule"></div>
  <h2 class="section-head">Transformative Services For Real Results</h2>

  <div class="card" style="left:141px">
    <div class="photo" style="background:linear-gradient(135deg,#ece6e2,#c9b7ab 50%,#e9ebed)" role="img" aria-label="Therapist listening to a troubled young woman on a sofa"></div>
    <h3>Individual Therapy</h3>
    <p>Lorem Ipsum is simply dummy text of the printing and typesetting industry. Lorem Ipsum has been the.</p>
    <div class="card-bottom" style="left:0"></div><div class="card-bottom" style="right:0"></div>
    <div class="card-icon"><svg width="26" height="26" viewBox="0 0 26 26" fill="none" stroke="#fff" stroke-width="1.6"><circle cx="13" cy="11" r="8"/><path d="M9 11h8M13 7v8M10 19v5h6v-5"/></svg></div>
  </div>
  <div class="card" style="left:459px">
    <div class="photo" style="background:linear-gradient(135deg,#dfe6ec,#8ea2b4 50%,#e3e8ec)" role="img" aria-label="Team of smiling doctors in white coats standing together"></div>
    <h3>Support Groups</h3>
    <p>Lorem Ipsum is simply dummy text of the printing and typesetting industry. Lorem Ipsum has been the.</p>
    <div class="card-bottom" style="left:0"></div><div class="card-bottom" style="right:0"></div>
    <div class="card-icon"><svg width="26" height="26" viewBox="0 0 26 26" fill="none" stroke="#fff" stroke-width="1.6"><circle cx="9" cy="8" r="3"/><circle cx="17" cy="8" r="3"/><circle cx="13" cy="16" r="3"/><path d="M4 16c0-2 2-4 5-4M22 16c0-2-2-4-5-4M8 24c0-2 2-4 5-4s5 2 5 4"/></svg></div>
  </div>
  <div class="card" style="left:778px">
    <div class="photo" style="background:linear-gradient(135deg,#2b4a6e,#5b86b1 50%,#c8d5df)" role="img" aria-label="Nurse supporting an elderly patient during a consultation"></div>
    <h3>Counseling</h3>
    <p>Lorem Ipsum is simply dummy text of the printing and typesetting industry. Lorem Ipsum has been the.</p>
    <div class="card-bottom" style="left:0"></div><div class="card-bottom" style="right:0"></div>
    <div class="card-icon"><svg width="26" height="26" viewBox="0 0 26 26" fill="none" stroke="#fff" stroke-width="1.6"><rect x="4" y="5" width="18" height="13" rx="2"/><path d="M8 18l-2 5 6-5M8 10h10M8 13h7"/></svg></div>
  </div>
</section>

<section class="journey">
  <div class="photo" role="img" aria-label="Doctor with a clipboard consulting a smiling young woman"></div>
  <div class="journey-copy">
    <h2>Ready To Begin<br>Your Journey To Wellness?</h2>
    <p>Get started on the path to health through the quality<br>medical care our team provides!</p>
    <div class="btn-ghost">Schedule Your Appointment</div>
  </div>
</section>

<section class="values">
  <div class="values-text"><span class="outline">Trustworthy_ </span><span class="solid">Caring_ </span><span class="outline">Professional</span></div>
</section>

<section class="reviews">
  <h2 class="section-head">What Our Clients Are Saying – Real Success Stories<br>from Trusted Partners</h2>

  <div class="review" style="left:-160px">
    <div class="quote" style="left:228px">”</div>
    <div class="stars" style="left:130px"><span class="off">★★</span></div>
    <p style="left:150px;width:120px">ummy text of the industry. Lorem ustry's standard he 1500s, when an galley of type.</p>
  </div>
  <div class="review" style="left:149px">
    <div class="quote orange" style="left:228px">”</div>
    <div class="avatar" role="img" aria-label="Client portrait"></div>
    <div class="stars">★★★<span class="off">★★</span></div>
    <h4>Milo Verant</h4>
    <p>Lorem Ipsum is simply dummy text of the printing and typesetting industry. Lorem Ipsum has been the industry's standard dummy text ever since the 1500s.</p>
  </div>
  <div class="review" style="left:457px">
    <div class="quote" style="left:228px">”</div>
    <div class="avatar" role="img" aria-label="Client portrait" style="background:linear-gradient(160deg,#c9ccd1,#4f5560)"></div>
    <div class="stars">★★★<span class="off">★★</span></div>
    <h4>Ezra Holloway</h4>
    <p>Lorem Ipsum is simply dummy text of the printing and typesetting industry. Lorem Ipsum has been the industry's.</p>
  </div>
  <div class="review" style="left:766px">
    <div class="quote orange" style="left:228px">”</div>
    <div class="avatar" role="img" aria-label="Client portrait" style="background:linear-gradient(160deg,#e2cfc3,#6b4a3d)"></div>
    <div class="stars">★★★<span class="off">★★</span></div>
    <h4>Nora Elwin</h4>
    <p>Lorem Ipsum is simply dummy text of the printing and typesetting industry. Lorem Ipsum has been the industry's standard dummy text ever since the 1500s, when an unknown printer took a galley of type.</p>
  </div>
  <div class="review" style="left:1074px">
    <div class="avatar" role="img" aria-label="Client portrait" style="background:linear-gradient(160deg,#d8cfc8,#3e3a3a)"></div>
    <div class="stars">★★★</div>
    <h4>Ilsa Marrow</h4>
    <p>Lorem Ipsum is simply dummy text of the printing and typesetting industry. Lorem Ipsum has been the industry's standard dummy text ever.</p>
  </div>

  <div class="dots"><i class="on"></i><i></i><i></i><i></i><i></i></div>
</section>

<footer class="site-footer">
  <div class="foot-brand"><span class="brand-dot"></span><span class="brand-name">Lumen Mind</span></div>
  <div class="foot-brand-sub">SERVICES</div>
  <p class="foot-about">Committed to providing expert mental health care in Washington DC, we empower individuals to heal, grow, and thrive</p>

  <div class="foot-col" style="left:368px">
    <h4>Quick Links</h4>
    <ul><li>Home</li><li>About Us</li><li>Sevices</li><li>Blog</li><li>FAQs</li><li>Contact Us</li></ul>
  </div>
  <div class="foot-col" style="left:526px;width:230px">
    <h4>Contact Info</h4>
    <p>2207 Alder Row Suite 4, Marlow,<br>Vermont 05344, United States</p>
    <p class="k">Email Address :</p>
    <p>info@lumenmindhealth.com</p>
    <p class="k">Phone Number :</p>
    <p>(555)-014-2290</p>
  </div>

  <div class="stay">
    <h4>Stay in Touch</h4>
    <p>Stay updated with health tips<br>and exclusive offers!</p>
    <div class="email">Email address <svg width="16" height="12" viewBox="0 0 16 12"><rect x="0.5" y="0.5" width="15" height="11" rx="1" fill="#9aa3b0"/><path d="M1 1l7 6 7-6" stroke="#fff" fill="none"/></svg></div>
    <div class="subscribe">Subscribe <svg width="14" height="14" viewBox="0 0 14 14"><path d="M1 1l12 6-12 6 3-6z" fill="#fff"/></svg></div>
  </div>

  <div class="foot-rule"></div>
  <div class="foot-bottom"><span>Copyright © 2025 Lumen Mind Health | All Rights Reserved.</span><span>Terms &amp; Condition &nbsp;|&nbsp; Privacy Policy &nbsp;|&nbsp; Support</span></div>
</footer>

</body>
</html>
```